Patient Fact sheets for medical conditions and treatments

Hi,

I need a new design for my patient fact sheets. I am moving from my current clinic and I am looking from a new look.

I have attached
1. a current Fact sheet
2. New home page to the website
3. New Logo.

They need to be single page and easily readable for patients.

The will be in both PDF and print form in the future.

Target Market(s)

Patients with chronic pain age 40+

Font styles to use
Serif

Requirements
Must have
• My logo, should be inline with design elements on the Front page provided.

Please use the same font as the Logo

```html
<!DOCTYPE html>
<html lang="en">
<head>
<meta charset="utf-8">
<title>Platelet Rich Plasma (PRP) Therapy – Fact Sheet</title>
<link href="https://fonts.googleapis.com/css2?family=Montserrat:wght@400;500;600&family=Nunito:wght@800;900&family=Tinos:wght@700&display=swap" rel="stylesheet">
<style>
  :root{
    --teal:#00b7c4;
    --teal-deep:#12a0ad;
    --ink:#2b3440;
    --text:#3a3f45;
    --orange:#f7a600;
    --rule:#f0d9a8;
    --paper:#ffffff;
    --backdrop:#ecebe8;
    --photo-a:#e9eef2;
    --photo-b:#c9d3da;
  }
  *{margin:0;padding:0;box-sizing:border-box}
  html,body{width:800px;height:1200px;overflow:hidden;background:var(--backdrop)}
  .sheet{position:absolute;left:9px;top:47px;width:782px;height:1105px;background:var(--paper);
    font-family:"Montserrat",Arial,sans-serif;color:var(--text);font-size:10.6px;line-height:12.7px;
    box-shadow:0 4px 18px rgba(0,0,0,.12)}
  .band{position:absolute;left:0;width:100%;height:12px;background:var(--orange)}
  .band--top{top:0}.band--bottom{bottom:0}
  .abs{position:absolute}
  .brand{left:35px;top:58px;display:flex;align-items:center;gap:8px}
  .brand__dot{width:22px;height:22px;border-radius:50%;background:var(--teal)}
  .brand__name{font-family:"Montserrat",sans-serif;font-weight:500;font-size:25px;color:var(--ink);line-height:1.05}
  .badge{left:304px;top:40px;width:478px;height:88px;background:var(--teal);color:#fff;
    font-family:"Montserrat",sans-serif;font-weight:600;font-size:58px;letter-spacing:4px;
    display:flex;align-items:center;justify-content:center}
  .title{left:35px;top:158px;font-family:"Nunito",sans-serif;font-weight:900;font-size:40px;line-height:52px;color:var(--teal-deep)}
  .title span{color:var(--ink)}
  .rule{left:35px;width:712px;height:1px;background:var(--rule)}
  .photo{left:35px;top:252px;width:341px;height:183px;border:1.5px solid var(--orange);
    background:linear-gradient(120deg,var(--photo-a) 0%,var(--photo-b) 45%,#f2d35a 60%,var(--photo-b) 75%,var(--photo-a) 100%)}
  .h{font-family:"Tinos",serif;font-weight:700;font-size:19.5px;line-height:22px;color:var(--ink);letter-spacing:.3px}
  .h em{font-style:normal;color:var(--teal-deep)}
  p + p{margin-top:12.7px}
  .col{width:345px}
  .ticks{list-style:none}
  .ticks li{position:relative;padding-left:20px;margin-bottom:8.4px}
  .ticks li svg{position:absolute;left:0;top:1px;width:11px;height:11px}
  .footer-text{font-size:9.3px;line-height:11px}
  .footer-text svg{width:9px;height:9px;vertical-align:-1px;margin-right:4px}
  .socials{display:flex;gap:9px;margin-top:5px;padding-left:14px}
  .socials span{width:9px;height:9px;background:#2e7bb8}
  .clinic-mark{left:352px;top:1044px;width:140px;font-family:"Montserrat",sans-serif;font-weight:600;font-size:10px;line-height:12px;color:var(--ink);letter-spacing:.5px}
  .disclaimer{left:503px;top:1022px;width:279px;height:58px;background:var(--teal-deep);color:#fff;padding:9px 14px;font-size:4.3px;line-height:5.2px}
  .disclaimer strong{display:block;font-size:5px;margin-bottom:2px}
</style>
</head>
<body>
<svg width="0" height="0" style="position:absolute">
  <symbol id="tick" viewBox="0 0 12 12"><circle cx="6" cy="6" r="6" fill="#f7a600"/><path d="M3.3 6.2l1.9 1.9 3.6-3.8" fill="none" stroke="#fff" stroke-width="1.6" stroke-linecap="round" stroke-linejoin="round"/></symbol>
</svg>

<main class="sheet">
  <div class="band band--top"></div>

  <div class="abs brand"><span class="brand__dot"></span><span class="brand__name">Harbourline<br>Pain Centre</span></div>
  <div class="abs badge">FACT SHEET</div>

  <h1 class="abs title">Platelet Rich Plasma (PRP) <span>Therapy</span></h1>
  <div class="abs rule" style="top:224px"></div>

  <div class="abs photo" role="img" aria-label="Gloved hand holding two test tubes of yellow platelet rich plasma"></div>

  <section class="abs col" style="left:406px;top:260px">
    <h2 class="h"><em>WHAT IS</em> PRP?</h2>
    <div style="margin-top:8px">
      <p>Platelet-Rich Plasma (PRP) is concentrated platelets and white blood cells derived from your own blood.</p>
      <p>Platelet Rich Plasma Injection Therapy (PRP therapy), is a growing treatment approach for soft tissue injuries including tendon, muscle and ligaments. It is also showing good results for mild to moderate osteoarthritis.</p>
      <p>While this approach has been used overseas for many years, it's fairly new to Australia in the treatment of musculo skeletal and orthopaedic conditions.</p>
    </div>
  </section>

  <section class="abs col" style="left:35px;top:458px">
    <h2 class="h"><em>HOW DOES</em> PRP WORK?</h2>
    <p style="margin-top:10px">Some tissues in the body have a poor blood supply or respond poorly to excessive load, ultimately failing to heal naturally. While some of our primary treatment such as physiotherapy, massage, biomechanical correction and other forms of treatment are used to treat these soft tissue injuries, sometimes the body fails to respond. PRP therapy utilises the healing properties in blood to allow a healing reaction to occur in a tissue that's not healing on its own. Our blood</p>
  </section>

  <p class="abs col" style="left:406px;top:466px">has small granules called 'platelets', which contain special growth factors that when released, allow stem cells in the particular tissue to 'switch' on and cause new tissue to be created and heal the injured area. Take the example of achilles tendinopathy. If the achilles is painful, thickened and not responding to rehabilitation, then the sports physician will inject the PRP into the achilles which will cause the tendon cells (tenocytes/fibroblasts) to create new achilles collagen to strengthen the achilles. White blood cells also enter the area to mop up any achilles tissue that may have been damaged due to the ongoing pain and thickening in the area.</p>

  <div class="abs rule" style="top:619px"></div>

  <section class="abs" style="left:35px;top:640px;width:712px">
    <h2 class="h"><em>ROLE OF PLATELETS &amp;</em> GROWTH FACTORS</h2>
    <p style="margin-top:8px;width:500px">PRP contains highly concentrated platelets. Platelets have been identified to secrete growth factors, which are known to play a role in:</p>
    <div style="display:flex;margin-top:14px">
      <ul class="ticks" style="width:370px">
        <li><svg><use href="#tick"/></svg>Increasing tissue vascularity and increasing the rate of<br>epithelial tissue production (wound healing)</li>
        <li><svg><use href="#tick"/></svg>Attracting other cells that fight infection</li>
        <li><svg><use href="#tick"/></svg>Acting as a seal during closures</li>
      </ul>
      <ul class="ticks">
        <li><svg><use href="#tick"/></svg>Providing an immediate surgical hemostatic agent<br>(reduction of bleeding)</li>
        <li><svg><use href="#tick"/></svg>Osteogenesis (bone regeneration and repair).</li>
      </ul>
    </div>
  </section>

  <div class="abs rule" style="top:800px"></div>

  <section class="abs" style="left:35px;top:820px;width:345px">
    <h2 class="h"><em>WHAT CAN</em> PRP TREAT?</h2>
    <p style="margin-top:8px">PRP therapy can be used for:</p>
    <div style="display:flex;margin-top:12px">
      <ul class="ticks" style="width:237px">
        <li><svg><use href="#tick"/></svg>Orthopedic surgery</li>
        <li><svg><use href="#tick"/></svg>Cardiac surgery</li>
        <li><svg><use href="#tick"/></svg>Plastic and cosmetic surgery</li>
        <li><svg><use href="#tick"/></svg>Ear, nose, throat (ENT) surgery</li>
        <li><svg><use href="#tick"/></svg>Oral maxillofacial surgery</li>
      </ul>
      <ul class="ticks">
        <li><svg><use href="#tick"/></svg>Neurosurgery</li>
        <li><svg><use href="#tick"/></svg>Vascular surgery</li>
        <li><svg><use href="#tick"/></svg>Wound healing</li>
        <li><svg><use href="#tick"/></svg>Burn care</li>
      </ul>
    </div>
    <p style="margin-top:1px">Ask your doctor whether plateletrich plasma is appropriate for your surgical procedure</p>
  </section>

  <section class="abs col" style="left:406px;top:816px">
    <h2 class="h"><em>WHAT ARE THE EXPECTED</em><br>RESULTS OF PRP?</h2>
    <p style="margin-top:12px">Because the goal of PRP therapy is to resolve pain through healing, it could prove to have lasting results. Initial improvement may be seen within a few weeks, gradually increasing as the healing progresses. Research studies and clinical practice have shown PRP therapy to be very effective at relieving pain and returning patients to their normal lives. The need for surgery can also be greatly reduced by treating injured tissues before the damage progresses and the condition is irreversible.</p>
  </section>

  <address class="abs footer-text" style="left:35px;top:1027px;font-style:normal">
    <div><svg viewBox="0 0 10 10"><path d="M5 0.5a3.2 3.2 0 0 0-3.2 3.2C1.8 6 5 9.5 5 9.5s3.2-3.5 3.2-5.8A3.2 3.2 0 0 0 5 .5zm0 4.4a1.2 1.2 0 1 1 0-2.4 1.2 1.2 0 0 1 0 2.4z" fill="#f7a600"/></svg>Harbourline Pain Centre, Level 2,</div>
    <div style="padding-left:13px">48 Wattle Street,<br>Brookvale VIC 3999</div>
    <div><svg viewBox="0 0 10 10"><rect x="0.5" y="2" width="9" height="6" fill="#f7a600"/><path d="M.5 2l4.5 3.5L9.5 2" fill="none" stroke="#fff" stroke-width=".8"/></svg>info@hlpain.example</div>
  </address>

  <div class="abs footer-text" style="left:230px;top:1027px;width:112px">
    <div><svg viewBox="0 0 10 10"><path d="M2.2 .8l1.6 2-1 1.1a6 6 0 0 0 3.3 3.3l1.1-1 2 1.6-.9 1.4C4.6 9 1 5.4.8 1.7z" fill="#f7a600"/></svg>03 9000 1234</div>
    <div><svg viewBox="0 0 10 10"><rect x="1" y="3" width="8" height="5" fill="#f7a600"/><rect x="2.5" y="1" width="5" height="2.5" fill="#f7a600"/></svg>03 9000 1235</div>
    <div><svg viewBox="0 0 10 10"><circle cx="5" cy="5" r="4.5" fill="#f7a600"/></svg>hlpain.example</div>
    <div class="socials"><span></span><span></span><span></span></div>
  </div>

  <div class="abs clinic-mark">RIDLEY<br>SPINE CARE</div>

  <aside class="abs disclaimer">
    <strong>DISCLAIMER</strong>
    Please note the contents of this patient fact sheet are general information only and are not a substitute for advice from your own health professional. Every patient's condition is different, and treatment plans are tailored to each person. Results may vary from patient to patient. If you would like to know whether this treatment suits you, please speak with one of our doctors at your next consultation.
  </aside>

  <div class="band band--bottom"></div>
</main>
</body>
</html>
```